Business card

would like a double sided business card made up with my logos provided.
Prefer card to have black background and to use the black logos, with matching blue writing for the text.
One side to just be the logo, (Try to use both the black logos)
the other side to have the logo and also my credentials/business information.

Covering all aspects of Carpentry and Building Services

Marcus Tolvey
Qualified Carpenter
Mob: 0417263948
Email: rkt.joinery@mailbright.com
ABN: 47 615 209 834

Industry/Entity Type

Business

Contact Information for Business Card

Marcus Tolvey
Qualified Carpenter
Mob: 0417263948
ABN: 47 615 209 834

Requirements
Must have
• Please try to use both the black logos and incorporate into the card.

```html
<!DOCTYPE html>
<html lang="en">
<head>
<meta charset="utf-8">
<title>RKT Joinery – Business Card</title>
<link rel="stylesheet" href="https://fonts.googleapis.com/css2?family=Arimo:wght@400;700&family=Open+Sans:wght@400&display=swap">
<style>
  :root {
    --page: #ffffff;
    --card-blue: #16a6da;
    --card-blue-deep: #0f93c9;
    --card-glow: #e9f7fd;
    --brand-ink: #2b2f33;
    --accent-blue: #15a4dc;
    --info-grey: #9a9ea3;
    --divider: #dfe3e6;
    --panel: #ffffff;
    --tagline: #ffffff;
  }
  * { box-sizing: border-box; margin: 0; padding: 0; }
  html, body {
    width: 1200px; height: 1200px; overflow: hidden;
    background: var(--page);
  }
  .canvas { position: relative; width: 1200px; height: 1200px; }

  .card {
    position: absolute; left: 228px; width: 727px; height: 412px;
    border-radius: 30px; overflow: hidden;
    background:
      radial-gradient(circle at var(--gx) var(--gy), var(--card-glow) 0, rgba(233,247,253,0.55) 90px, rgba(22,166,218,0) 230px),
      linear-gradient(160deg, #2bb6e6 0%, var(--card-blue) 45%, var(--card-blue-deep) 100%);
    font-family: "Arimo", Arial, sans-serif;
  }
  .card--front { top: 122px; --gx: 140px; --gy: 150px; }
  .card--back { top: 639px; --gx: 150px; --gy: 120px; }

  .brand {
    position: absolute; display: flex; align-items: center;
    color: var(--brand-ink); font-weight: 700; white-space: nowrap;
    letter-spacing: 0.5px;
  }
  .brand__mark { background: var(--brand-ink); flex: none; }
  .card--front .brand { left: 22px; top: 132px; font-size: 31px; gap: 8px; }
  .card--front .brand__mark { width: 14px; height: 14px; }
  .card--back .brand { left: 74px; top: 98px; font-size: 54px; gap: 12px; }
  .card--back .brand__mark { width: 22px; height: 22px; }

  .details {
    position: absolute; left: 291px; top: 42px; width: 390px; height: 326px;
    background: var(--panel); border-radius: 6px;
    box-shadow: 0 4px 14px rgba(0, 60, 100, 0.25);
  }
  .details__pointer { position: absolute; left: -13px; top: 80px; width: 14px; height: 24px; }
  .details__name {
    position: absolute; left: 28px; top: 24px;
    font-size: 41px; font-weight: 700; color: var(--accent-blue);
  }
  .details__role {
    position: absolute; left: 28px; top: 78px;
    font-size: 26px; color: var(--accent-blue);
  }
  .details__rule {
    position: absolute; left: 0; right: 0; top: 130px;
    height: 2px; background: var(--divider);
  }
  .details__list { list-style: none; position: absolute; left: 28px; top: 148px; }
  .details__list li { font-size: 22px; color: var(--info-grey); line-height: 45px; }
  .details__list li.email { font-size: 21px; }

  .pill {
    position: absolute; left: 338px; width: 326px; height: 44px;
    background: linear-gradient(#ffffff, #eef6fa);
    border-radius: 22px;
    box-shadow: 0 3px 8px rgba(0, 60, 100, 0.3);
    color: var(--accent-blue); font-weight: 700; font-size: 27px;
    display: flex; align-items: center; padding-left: 22px;
  }
  .pill__tail { position: absolute; left: 4px; bottom: -13px; width: 20px; height: 16px; }
  .pill--mobile { top: 184px; }
  .pill--abn { top: 277px; }

  .tagline {
    position: absolute; left: 40px; top: 358px;
    font-family: "Open Sans", Arial, sans-serif;
    font-size: 19px; color: var(--tagline);
  }
</style>
</head>
<body>
<main class="canvas">

  <section class="card card--front" aria-label="Business card front">
    <div class="brand"><span class="brand__mark"></span>RKT JOINERY</div>

    <div class="details">
      <svg class="details__pointer" viewBox="0 0 14 24" aria-hidden="true">
        <polygon points="14,0 0,12 14,24" fill="#ffffff"/>
      </svg>
      <h1 class="details__name">Marcus Tolvey</h1>
      <p class="details__role">Qualified Carpenter</p>
      <div class="details__rule"></div>
      <ul class="details__list">
        <li class="email">Email: rkt.joinery@mailbright.com</li>
        <li>ABN: 47 615 209 834</li>
        <li>Mobile: 0417263948</li>
      </ul>
    </div>
  </section>

  <section class="card card--back" aria-label="Business card back">
    <div class="brand"><span class="brand__mark"></span>RKT JOINERY</div>

    <div class="pill pill--mobile">
      <svg class="pill__tail" viewBox="0 0 20 16" aria-hidden="true">
        <polygon points="4,0 20,0 2,16" fill="#eef6fa"/>
      </svg>
      Mobile: 0417263948
    </div>
    <div class="pill pill--abn">
      <svg class="pill__tail" viewBox="0 0 20 16" aria-hidden="true">
        <polygon points="4,0 20,0 2,16" fill="#eef6fa"/>
      </svg>
      ABN: 47 615 209 834
    </div>

    <p class="tagline">Covering all aspects of Carpentry and Building Services</p>
  </section>

</main>
</body>
</html>
```